Business Card Design Needed

Business car design required, logo will be supplied.

Brambleford Power Surveyors are looking to become the leading provider of energy performance certificates to estate agents, landlords and home owners in the Yorkshire region of the UK.

The business card must be double sided and professional looking. Estate agents receive hundreds of cards from contractors and our card must stand out.

I require a two sided business card that is clean, modern and created by a designer that can think outside of the box.

Brand colours can be supplied .

Please ask if you have any questions.

Target Market(s)

Estate agents, landlords and property owners

Industry/Entity Type

Property - estate agency - energy consultants

Contact Information for Business Card

Tomas Rendell - Energy Assessor - 07311642705 - www.BramblefordPSV.co.uk - info@bramblefordpsv.co.uk

Font styles to use
Serif
Sans Serif

Colors
00AB8E
00BBA5
67D7C9
C6EFE9
E9F9F6

Requirements
Must have
• Use the provided logo, clean, professional and stand out from the crowd
Nice to have
• Clever use of text, spacing and brand colours
Should not have
• Clip art

```html
<!DOCTYPE html>
<html lang="en">
<head>
<meta charset="utf-8">
<title>Brambleford Power Surveyors – Business Card</title>
<link rel="stylesheet" href="https://fonts.googleapis.com/css2?family=Poppins:wght@300;400;500&display=swap">
<style>
  :root {
    --backdrop: #2b2b2d;
    --card-white: #ffffff;
    --brand-blue: #0a66ab;
    --brand-blue-deep: #08578f;
    --brand-blue-light: #1487d0;
    --brand-lime: #b6cc1a;
    --text-grey: #3d3d3f;
    --rule-grey: #9a9a9a;
  }
  * { box-sizing: border-box; margin: 0; padding: 0; }
  html, body {
    width: 1200px;
    height: 1108px;
    overflow: hidden;
    background: var(--backdrop);
    font-family: "Poppins", sans-serif;
  }
  .stage {
    position: relative;
    width: 1200px;
    height: 1108px;
    display: flex;
    justify-content: center;
    align-items: center;
    gap: 60px;
  }
  .card {
    position: relative;
    width: 340px;
    height: 540px;
    border-radius: 22px;
    overflow: hidden;
    box-shadow: 0 14px 30px rgba(0,0,0,0.45);
  }

  /* Front */
  .card--front {
    background: var(--card-white);
    display: flex;
    flex-direction: column;
    align-items: center;
  }
  .brand {
    margin-top: 120px;
    display: flex;
    align-items: center;
    gap: 14px;
  }
  .brand__dot {
    width: 40px;
    height: 40px;
    border-radius: 50%;
    background: var(--brand-lime);
    flex: none;
  }
  .brand__name {
    color: var(--brand-blue);
    font-weight: 400;
    font-size: 21px;
    line-height: 1.15;
    letter-spacing: 0.5px;
  }
  .person {
    margin-top: 150px;
    text-align: center;
  }
  .person__name {
    color: var(--brand-blue);
    font-weight: 400;
    font-size: 25px;
    letter-spacing: 0.3px;
    text-transform: uppercase;
  }
  .person__role {
    color: var(--brand-lime);
    font-weight: 400;
    font-size: 14px;
    text-transform: uppercase;
    margin-top: 2px;
  }
  .icon-rule {
    margin-top: 12px;
    display: flex;
    align-items: center;
    gap: 6px;
  }
  .icon-rule__line {
    width: 54px;
    height: 1px;
    background: var(--rule-grey);
  }
  .icon-rule__icon {
    width: 28px;
    height: 28px;
    border-radius: 5px;
    background: var(--brand-blue);
    display: flex;
    align-items: center;
    justify-content: center;
  }
  .contact {
    margin-top: 10px;
    text-align: center;
    color: var(--text-grey);
    font-weight: 300;
    font-size: 15px;
    line-height: 1.4;
  }
  .contact__web-name { color: var(--brand-blue); }

  /* Back */
  .card--back {
    background: var(--brand-blue);
  }
  .card__pattern {
    position: absolute;
    inset: 0;
    background: linear-gradient(225deg, var(--brand-blue-light) 0%, var(--brand-blue) 45%, var(--brand-blue-deep) 100%);
  }
  .back-brand {
    position: absolute;
    left: 50%;
    top: 50%;
    transform: translate(-50%, -50%);
    display: flex;
    align-items: center;
    gap: 10px;
  }
  .back-brand__dot {
    width: 30px;
    height: 30px;
    border-radius: 50%;
    background: var(--brand-lime);
  }
  .back-brand__name {
    color: var(--card-white);
    font-weight: 400;
    font-size: 16px;
    letter-spacing: 0.5px;
  }
</style>
</head>
<body>
<main class="stage">
  <section class="card card--front">
    <div class="brand">
      <span class="brand__dot"></span>
      <span class="brand__name">Brambleford<br>Power Surveyors</span>
    </div>

    <div class="person">
      <h1 class="person__name">Tomas Rendell</h1>
      <p class="person__role">Energy Assessor</p>
    </div>

    <div class="icon-rule">
      <span class="icon-rule__line"></span>
      <span class="icon-rule__icon" aria-label="Phone">
        <svg width="16" height="16" viewBox="0 0 16 16"><path d="M4 2l2 3-1.3 1.3a8 8 0 0 0 5 5L11 10l3 2-1 2.3C7 14 2 9 1.7 3z" fill="#fff"/></svg>
      </span>
      <span class="icon-rule__icon" aria-label="Email">
        <svg width="16" height="16" viewBox="0 0 16 16"><rect x="1.5" y="3.5" width="13" height="9" fill="none" stroke="#fff" stroke-width="1.3"/><path d="M1.5 3.5L8 9l6.5-5.5" fill="none" stroke="#fff" stroke-width="1.3"/></svg>
      </span>
      <span class="icon-rule__icon" aria-label="Website">
        <svg width="16" height="16" viewBox="0 0 16 16"><circle cx="8" cy="8" r="6.3" fill="none" stroke="#fff" stroke-width="1.3"/><ellipse cx="8" cy="8" rx="2.6" ry="6.3" fill="none" stroke="#fff" stroke-width="1.1"/><path d="M1.8 8h12.4" stroke="#fff" stroke-width="1.1"/></svg>
      </span>
      <span class="icon-rule__line"></span>
    </div>

    <div class="contact">
      <p>07311642705</p>
      <p>info@bramblefordpsv.co.uk</p>
      <p>www.<span class="contact__web-name">BramblefordPSV</span>.co.uk</p>
    </div>
  </section>

  <section class="card card--back">
    <div class="card__pattern" role="img" aria-label="Embossed repeating brand-mark pattern in tonal blues"></div>
    <div class="back-brand">
      <span class="back-brand__dot"></span>
      <span class="back-brand__name">Brambleford</span>
    </div>
  </section>
</main>
</body>
</html>
```